Risk Management Company in need of Business Card Design

We sell risk management insurance to Lenders (Banks, Credit Unions, Real Estate Trust).

We need a very clean, professional card that will leave a great impression.

We are looking to use a blue color for our logo on the card (Preferably close to royal blue but are open to looking at navy blue or any darker blues as well).

Please see the logo attached to get an idea. We are open to writing Harbor Shield Under the logo or next to the logo. Really whatever looks best.

Target Market(s)

Banks, Credit Unions, Real Estate Trusts

Industry/Entity Type

Insurance

Contact Information for Business Card

Name: Mark Dunstan
Title: Regional Sales Director
Email: mdunstan@harborshield.example
C:555-555-0143
D:555-555-0187
800-555-0129 Ext.205
F:555-555-0164 (We would like to see some cards without the fax number as well to compare)

Company Name: Harbor Shield
Website: www.harborshield.example

Address: 118 E. Morrow St. Suite 420, Eastbrook, PA 21299 (Preferably written on the bottom of the card in small print.)

Colors
0355a3
0455a3

Requirements
Nice to have
• We would like to see a couple of where the back has the logo in reverse colors (Logo White, Background Blue)

```html
<!DOCTYPE html>
<html lang="en">
<head>
<meta charset="utf-8">
<title>Harbor Shield – Business Card</title>
<link href="https://fonts.googleapis.com/css2?family=Cinzel:wght@400;600&display=swap" rel="stylesheet">
<style>
  :root {
    --navy: #22234f;
    --paper: #fbfbf9;
    --silver: #dcdcde;
    --ink: #1a1a1a;
    --white: #ffffff;
    --stage: #eeeeee;
  }
  * { margin: 0; padding: 0; box-sizing: border-box; }
  html, body { width: 1200px; height: 1000px; overflow: hidden; }
  body {
    background: var(--stage);
    font-family: "Cinzel", serif;
    position: relative;
  }

  /* Back of card */
  .card-back {
    position: absolute;
    left: 460px; top: 110px;
    width: 700px; height: 440px;
    background: var(--navy);
    box-shadow: 0 6px 18px rgba(0,0,0,.18);
  }
  .card-back .brand {
    position: absolute;
    left: 70px; top: 150px;
    display: flex; align-items: center; gap: 28px;
    color: var(--silver);
  }
  .card-back .brand-mark { width: 70px; height: 70px; background: var(--silver); }
  .card-back .brand-name { font-size: 48px; font-weight: 400; letter-spacing: 3px; white-space: nowrap; }

  /* Front of card */
  .card-front {
    position: absolute;
    left: 60px; top: 405px;
    width: 700px; height: 445px;
    background: var(--paper);
    box-shadow: 0 8px 22px rgba(0,0,0,.22);
    color: var(--ink);
  }
  .divider { position: absolute; width: 3px; }
  .divider.upper { left: 367px; top: 20px; height: 272px; background: var(--navy); }

  .identity {
    position: absolute; left: 0; top: 0; width: 367px; height: 315px;
    text-align: center;
  }
  .identity .brand {
    position: absolute; left: 0; right: 0; top: 80px;
    display: flex; justify-content: center; align-items: center; gap: 12px;
    color: var(--navy);
  }
  .identity .brand-mark { width: 24px; height: 24px; background: var(--navy); }
  .identity .brand-name { font-size: 23px; font-weight: 600; letter-spacing: 2px; white-space: nowrap; }
  .identity .person-name {
    position: absolute; left: 0; right: 0; top: 200px;
    font-size: 32px; letter-spacing: 3px; font-weight: 400; white-space: nowrap;
  }
  .identity .person-title {
    position: absolute; left: 0; right: 0; top: 252px;
    font-size: 15px; font-style: italic; letter-spacing: 2px; white-space: nowrap;
  }

  .contact { position: absolute; left: 385px; top: 118px; width: 305px; }
  .contact .email { font-size: 10.5px; letter-spacing: 1px; margin-bottom: 8px; white-space: nowrap; }
  .contact .email b { font-weight: 600; }
  .contact .row { display: flex; align-items: baseline; font-size: 17px; line-height: 28px; letter-spacing: 1.5px; white-space: nowrap; }
  .contact .label { width: 78px; text-align: right; padding-right: 18px; font-size: 12px; letter-spacing: 2px; }

  .footer-band {
    position: absolute; left: 0; right: 0; bottom: 0; height: 125px;
    background: var(--navy); color: var(--white);
  }
  .divider.lower { left: 369px; top: 20px; height: 88px; background: var(--white); }
  .footer-band .web {
    position: absolute; left: 0; width: 369px; top: 53px;
    text-align: center; font-size: 12.5px; letter-spacing: 1.5px; color: var(--white);
  }
  .footer-band .address {
    position: absolute; left: 390px; top: 32px; width: 300px;
    text-align: center;
    font-size: 12.5px; line-height: 28px; letter-spacing: 1.5px; color: var(--white);
    white-space: nowrap;
  }
</style>
</head>
<body>
  <section class="card-back" aria-label="Card back">
    <div class="brand">
      <span class="brand-mark"></span>
      <span class="brand-name">HARBOR SHIELD</span>
    </div>
  </section>

  <section class="card-front" aria-label="Card front">
    <div class="identity">
      <div class="brand">
        <span class="brand-mark"></span>
        <span class="brand-name">HARBOR SHIELD</span>
      </div>
      <h1 class="person-name">Mark Dunstan</h1>
      <p class="person-title">Regional Sales Director</p>
    </div>
    <span class="divider upper"></span>

    <div class="contact">
      <p class="email"><b>EMAIL:</b> MDUNSTAN@HARBORSHIELD.EXAMPLE</p>
      <p class="row"><span class="label">Cell:</span>555-555-0143</p>
      <p class="row"><span class="label">D:</span>555-555-0187</p>
      <p class="row"><span class="label"></span>800-555-0129</p>
      <p class="row"><span class="label">F:</span>555-555-0164</p>
    </div>

    <div class="footer-band">
      <p class="web">WWW.HARBORSHIELD.EXAMPLE</p>
      <span class="divider lower"></span>
      <p class="address">118 E. Morrow St.<br>Suite 420, Eastbrook, PA 21299</p>
    </div>
  </section>
</body>
</html>
```